Web Design Project

We need a website design for a new website. The site will have two parts, a sales and marketing site (nothing exists at present) and an online business application, which is under construction.
The sales and marketing site needs a top level menu, and area to log into or sign up to the online applciation. Other than that we are open to suggestions.
The onlne applciations needs a similar look/feel to the marketing site and it's design needs to incorporate the following parts:
- grids
- settings page
- pop up boxes
- error messages
Please create an account on the development site at http://vorlindesk.hostpad.net to see waht functionality needs to be incorporated in the design. Needs to be viewed in FireFox.
The logo we have chosen for the site has been uploaded, please ensure all designs fit with this. I have no problems if you wish to make alterations to the logo.
- Design for both the marketing site and online application.

```html
<!DOCTYPE html>
<html lang="en">
<head>
<meta charset="utf-8">
<title>vorlindesk – Add Expense</title>
<link href="https://fonts.googleapis.com/css2?family=Arimo:wght@400;700&family=Didact+Gothic&display=swap" rel="stylesheet">
<style>
:root{
  --page:#ffffff;
  --brand-green:#4a9d2e;
  --brand-blue:#1f6fb8;
  --grid-head:#1d9a1f;
  --grid-body:#95d220;
  --rule:#e9f5d0;
  --menu-top:#1b94d6;
  --menu-bottom:#0a5c93;
  --ink:#111;
  --muted:#8a8a8a;
  --nav-ink:#666;
  --link:#1f6fb8;
  --field:#ffffff;
  --field-line:#c9d6c2;
}
*{box-sizing:border-box;margin:0;padding:0}
html,body{width:1200px;height:366px;overflow:hidden;background:var(--page)}
body{position:relative;font-family:"Arimo",Arial,sans-serif;color:var(--ink)}
.abs{position:absolute}
.caps{font-family:"Didact Gothic",Arial,sans-serif;white-space:nowrap}

/* header */
.brand{left:8px;top:14px;display:flex;align-items:flex-end;gap:8px}
.brand-mark{width:26px;height:26px;background:var(--brand-blue);margin-bottom:8px}
.brand-name{font-family:"Didact Gothic",sans-serif;font-size:42px;line-height:42px;color:var(--brand-green)}
.company{font-size:13px;color:var(--muted);margin-bottom:6px}
.company span{color:var(--brand-blue)}
.user-nav a{position:absolute;top:22px;display:flex;flex-direction:column;align-items:center;font-size:12px;letter-spacing:.9px;color:var(--nav-ink);text-decoration:none}
.user-nav svg{width:16px;height:16px;margin-bottom:4px}

/* tabs */
.tabs{top:103px;font-size:11px;color:var(--nav-ink)}
.tabs.on{color:var(--link)}

/* grid header */
.grid-head{left:196px;top:93px;width:1004px;height:33px;background:var(--grid-head)}
.col-label{top:102px;color:#fff;font-size:13px;letter-spacing:.9px}
.select-all{left:1115px;top:100px;width:21px;height:17px;background:#fff}

/* body */
.grid-body{left:0;top:126px;width:1200px;height:145px;background:var(--grid-body)}
.divider{top:93px;width:1px;height:178px;background:var(--rule)}

/* side menu */
.menu-item{left:0;width:196px;height:36px;padding-left:22px;display:flex;align-items:center;color:#fff;font-size:13px;letter-spacing:.8px}
.menu-item.nav{background:linear-gradient(var(--menu-top),var(--menu-bottom));border-top:1px solid #5ab7e8}

/* fields */
.field{background:var(--field);border:1px solid var(--field-line);height:17px}
.select{position:absolute}
.select::after{content:"";position:absolute;right:0;top:0;width:14px;height:15px;border-left:1px solid var(--field-line);background:linear-gradient(#fff,#e6e6e6)}
.select::before{content:"";position:absolute;right:4px;top:6px;border:3px solid transparent;border-top-color:#999;z-index:1}
.lbl{font-size:9px;white-space:nowrap}
.date{left:206px;top:140px;width:66px;font-size:9px;text-align:center;line-height:15px}
.hint{left:344px;top:213px;font-size:8px;font-style:italic}
.browse{left:428px;top:193px;font-size:9px;color:#fff;font-weight:700}
.upload-go{left:405px;top:190px;width:15px;height:15px;background:#1b8fd8;border:1px solid #fff}
.btn{left:1115px;width:46px;height:10px;border:1px solid #2a5da8;background:#fff;font-size:5px;font-weight:700;color:#2a5da8;display:flex;align-items:center;gap:3px;letter-spacing:.3px}
.btn i{display:block;width:9px;height:8px;margin-left:-1px}
.footer-label{left:293px;top:284px;font-size:10.5px;white-space:nowrap}
.page-code{left:1170px;top:338px;font-size:12px;letter-spacing:1px;color:#444}
</style>
</head>
<body>

<header>
  <div class="abs brand">
    <div class="brand-mark"></div>
    <div class="brand-name">vorlindesk</div>
    <div class="company">company name <span>Q7 Systems</span></div>
  </div>
  <nav class="user-nav caps">
    <a href="#" style="left:954px"><svg viewBox="0 0 16 16"><circle cx="8" cy="5" r="3.5" fill="#3a7fd0"/><path d="M2 15c0-4 3-6 6-6s6 2 6 6z" fill="#3a7fd0"/></svg>WELCOME USER</a>
    <a href="#" style="left:1073px"><svg viewBox="0 0 16 16"><path d="M5 7V4.5a3 3 0 0 1 6 0" stroke="#3a7fd0" stroke-width="2" fill="none"/><rect x="1" y="7" width="11" height="8" fill="#2f6fc4"/></svg>LOG OUT</a>
    <a href="#" style="left:1145px"><svg viewBox="0 0 16 16"><path d="M13 8a5 5 0 1 1-2-4" stroke="#3a7fd0" stroke-width="2.4" fill="none"/><path d="M9 2h4v4z" fill="#3a7fd0"/></svg>LOGIN</a>
  </nav>
</header>

<span class="abs tabs on caps" style="left:20px">UNCLAIMED <span style="color:var(--nav-ink)">(0)</span></span>
<span class="abs tabs caps" style="left:109px">REJECTED (0)</span>

<div class="abs grid-body"></div>
<div class="abs grid-head"></div>
<div class="abs divider" style="left:286px"></div>
<div class="abs divider" style="left:656px"></div>
<div class="abs divider" style="left:735px"></div>
<div class="abs divider" style="left:859px"></div>
<div class="abs divider" style="left:993px"></div>
<div class="abs divider" style="left:1105px"></div>

<span class="abs col-label caps" style="left:222px">DATE</span>
<span class="abs col-label caps" style="left:315px">DESCRIPTION</span>
<span class="abs col-label caps" style="left:677px">CLASS</span>
<span class="abs col-label caps" style="left:754px">CLIENT NAME</span>
<span class="abs col-label caps" style="left:879px">PROJECT NAME</span>
<span class="abs col-label caps" style="left:1012px">AMOUNT</span>
<div class="abs select-all"></div>

<nav>
  <div class="abs menu-item caps" style="top:126px">ADD EXPENSE</div>
  <div class="abs menu-item nav caps" style="top:162px">CLAIM MANAGEMENT</div>
  <div class="abs menu-item nav caps" style="top:198px">SETTINGS</div>
  <div class="abs menu-item nav caps" style="top:235px">USER MANAGEMENT</div>
</nav>

<div class="abs field date">31/12/2011</div>

<span class="abs lbl" style="left:293px;top:145px"><b>EXPENSE:</b> DESCRIPTION</span>
<div class="abs field" style="left:409px;top:141px;width:66px"></div>
<div class="field select" style="left:480px;top:141px;width:77px"></div>
<span class="abs lbl" style="left:567px;top:145px">NOTES</span>

<span class="abs lbl" style="left:293px;top:169px">TAX AMOUNT: $</span>
<div class="abs field" style="left:368px;top:165px;width:66px"></div>
<span class="abs lbl" style="left:449px;top:169px">PAYMENT METHOD</span>

<span class="abs lbl" style="left:293px;top:193px">UPLOAD</span>
<div class="abs field" style="left:344px;top:190px;width:62px;height:15px"></div>
<div class="abs upload-go"><svg viewBox="0 0 15 15" width="13" height="13"><path d="M3 7.5h7M7 4l3.5 3.5L7 11" stroke="#fff" stroke-width="2" fill="none"/></svg></div>
<span class="abs browse">browse</span>
<span class="abs hint">drop files here to upload</span>

<div class="abs field" style="left:661px;top:142px;width:66px"></div>
<div class="field select" style="left:755px;top:142px;width:78px"></div>
<div class="field select" style="left:879px;top:142px;width:78px"></div>
<span class="abs lbl" style="left:1003px;top:146px;font-size:10px">$</span>
<div class="abs field" style="left:1015px;top:142px;width:66px"></div>

<div class="abs btn" style="top:143px"><i style="background:#2da52d"><svg viewBox="0 0 9 8" width="9" height="8"><path d="M1.5 4l2 2 4-4.5" stroke="#fff" stroke-width="1.4" fill="none"/></svg></i>SAVE</div>
<div class="abs btn" style="top:157px"><i style="background:#d8261b"><svg viewBox="0 0 9 8" width="9" height="8"><path d="M1.5 4h6" stroke="#fff" stroke-width="1.6"/></svg></i>CANCEL</div>

<span class="abs footer-label">ADD EXPENSE</span>
<div class="field select" style="left:372px;top:282px;width:79px;height:16px"></div>

<span class="abs page-code caps">X15</span>

</body>
</html>
```